Vantrel Telecom Corporate Website & Social Branding

We are looking for a new website for our startup telecom which provides UCaaS, SD-WAN, Business SMS/MMS, Video Conferencing, Managed Network Service & more.

Target Market(s)

Small offices from 1-250 users

Industry/Entity Type

Telecomunications

Coding

Coded - Design and coding required

Colors
0054AA
0677BA
7BADD7
CADEEF
E8F1F8

```html
<!DOCTYPE html>
<html lang="en">
<head>
<meta charset="utf-8">
<title>Vantrel Telecom</title>
<link href="https://fonts.googleapis.com/css2?family=Montserrat:wght@300;400;500;600;700&display=swap" rel="stylesheet">
<style>
:root{
  --navy:#0054AA;
  --blue:#0677BA;
  --sky:#7BADD7;
  --mist:#CADEEF;
  --ice:#E8F1F8;
  --ink:#231f20;
  --dark:#252330;
  --text:#3c3c3c;
  --white:#ffffff;
}
*{box-sizing:border-box;margin:0;padding:0}
html,body{width:1200px;height:2866px;overflow:hidden}
body{position:relative;font-family:'Montserrat',sans-serif;color:var(--text);background:var(--white)}
.abs{position:absolute}
/* header */
.site-header{left:0;top:0;width:1200px;height:72px;background:var(--blue)}
.brand{left:142px;top:25px;display:flex;align-items:center;gap:7px;color:var(--white);font-weight:700;font-size:15px;white-space:nowrap}
.brand-dot{width:20px;height:20px;border-radius:50%;background:var(--navy);border:2px solid var(--white);flex:none}
.main-nav{left:342px;top:28px;display:flex;gap:29px;font-size:12px;font-weight:500;color:var(--white);white-space:nowrap}
.header-cta{left:894px;top:20px;width:160px;height:32px;background:#0a4f82;color:var(--white);font-size:12px;font-weight:600;display:flex;align-items:center;justify-content:center;border-radius:2px}
/* hero */
.hero{left:0;top:72px;width:1200px;height:484px;background:linear-gradient(110deg,#2b2640 0%,#1f2a44 45%,#2c2f3e 100%)}
.hero-title{left:142px;top:222px;color:var(--white)}
.hero-title strong{display:block;font-size:21px;font-weight:700;margin-bottom:4px}
.hero-title span{display:block;font-size:25px;font-weight:300;line-height:34px;white-space:nowrap;letter-spacing:-.2px}
.btn{display:flex;align-items:center;justify-content:center;font-size:14px;color:var(--white)}
.btn-primary{left:142px;top:373px;width:165px;height:41px;background:var(--blue);border:1px solid var(--sky)}
.btn-ghost{left:314px;top:373px;width:180px;height:41px;border:1px solid var(--white)}
.laptop{left:636px;top:139px;width:445px;height:300px;border:8px solid #d9dde2;border-radius:10px 10px 0 0;background:linear-gradient(135deg,#6f8fb1,#4a6e96 55%,#2c4a74)}
.laptop-base{left:585px;top:437px;width:547px;height:14px;background:linear-gradient(#e6e8ea,#9aa0a6);border-radius:0 0 20px 20px}
.play{left:800px;top:262px;width:120px;text-align:center;color:var(--white);font-size:15px;font-weight:600;letter-spacing:3px}
.play svg{display:block;margin:0 auto 8px}
/* services */
.section-title{left:0;width:1200px;text-align:center;font-size:28px;font-weight:700;color:var(--ink)}
.section-title .light{font-weight:300;color:var(--blue)}
.card{width:282px;height:293px;background:var(--white);box-shadow:0 1px 6px rgba(0,0,0,.12);padding:36px 14px 0 20px}
.card.featured{background:var(--dark)}
.card svg{display:block;height:66px;margin-bottom:20px}
.card h3{font-size:18px;font-weight:500;color:var(--ink);margin-bottom:6px;white-space:nowrap}
.card p{font-size:12.6px;line-height:17.6px;padding-left:6px;margin-bottom:12px;letter-spacing:-.15px}
.card a{font-size:13px;padding-left:6px;color:var(--text);text-decoration:underline}
.card.featured h3,.card.featured p,.card.featured a{color:var(--blue)}
/* testimonials */
.quote-card{width:282px;height:339px;background:var(--white);border-bottom:4px solid var(--navy);padding:22px 12px 0 16px;display:flex;flex-direction:column}
.quote-card.featured{background:var(--blue);color:var(--white);border-bottom-color:var(--dark)}
.quote-card svg{flex:none}
.quote-card p{font-size:12.8px;line-height:20.8px;margin:14px 0 12px;letter-spacing:-.15px}
.quote-card h4{font-size:16.5px;font-weight:500;color:var(--ink);line-height:20px}
.quote-card small{font-size:12px;font-weight:500;color:var(--ink);line-height:16px}
.quote-card.featured h4,.quote-card.featured small{color:var(--white)}
/* trial */
.trial-title{left:142px;top:2040px;font-size:26px;font-weight:700;color:var(--blue)}
.trial-text{left:144px;top:2090px;width:450px;font-size:12.5px;line-height:18px}
.field{left:144px;width:361px;height:51px;border:1px solid #bfc6cd;font-size:12.5px;color:#555;display:flex;align-items:center;padding-left:18px;background:var(--white)}
.field.select{justify-content:space-between;padding-right:16px}
.submit{left:144px;top:2463px;width:150px;height:31px;background:var(--blue);color:var(--white);font-size:13px;font-weight:600;display:flex;align-items:center;justify-content:center;box-shadow:0 3px 5px rgba(0,0,0,.2)}
.illustration{left:487px;top:2156px;width:713px;height:447px;background:linear-gradient(180deg,#f3f5f2,#e9eeec)}
/* footer */
.site-footer{left:0;top:2603px;width:1200px;height:263px;background:var(--navy);color:var(--white)}
.footer-brand{left:142px;top:2664px;display:flex;align-items:center;gap:8px;font-size:19px;font-weight:700;color:var(--white);white-space:nowrap}
.footer-brand .brand-dot{width:26px;height:26px}
.footer-copy{left:142px;top:2740px;font-size:12.5px;line-height:24px;color:var(--white);font-weight:500}
.footer-col h5{font-size:16px;font-weight:600;margin-bottom:12px}
.footer-col li{list-style:none;font-size:12.5px;font-weight:600;line-height:24.5px;white-space:nowrap}
.divider{width:1px;height:146px;background:rgba(255,255,255,.45);top:2648px}
.social{display:flex;gap:10px}
.social span{width:23px;height:23px;border-radius:50%;background:var(--white)}
</style>
</head>
<body>

<header class="site-header abs">
  <div class="brand abs"><span class="brand-dot"></span>Vantrel Telecom</div>
  <nav class="main-nav abs"><span>Products</span><span>Integrations</span><span>Features</span><span>Pricing</span><span>Blog</span><span>Sign In</span></nav>
  <div class="header-cta abs">Start Your Free Trial</div>
</header>

<section class="hero abs" role="img" aria-label="Dimly lit server room background"></section>
<div class="hero-title abs">
  <strong>Telecom Provides</strong>
  <span>UCaaS, SD-WAN, Business SMS/MMS</span>
  <span>Video Conferencing, Managed Network</span>
  <span>Service &amp; more.</span>
</div>
<div class="btn btn-primary abs">LEARN MORE</div>
<div class="btn btn-ghost abs">REQUEST A QUOTE</div>
<div class="laptop abs" role="img" aria-label="Laptop showing a support agent wearing a headset"></div>
<div class="laptop-base abs"></div>
<div class="play abs">
  <svg width="42" height="42" viewBox="0 0 42 42"><circle cx="21" cy="21" r="19" fill="none" stroke="#fff" stroke-width="2"/><path d="M17 12 L29 21 L17 30 Z" fill="none" stroke="#fff" stroke-width="2"/></svg>
  PLAY NOW
</div>

<svg class="abs" style="left:0;top:556px" width="1200" height="46" viewBox="0 0 1200 46"><path d="M0 0H1200V14H1054V44L600 28L142 42V14H0Z" fill="var(--blue)"/></svg>

<svg class="abs" style="left:0;top:940px" width="1200" height="560" viewBox="0 0 1200 560"><path d="M0 5 L1200 45 L1200 555 L0 488 Z" fill="var(--blue)"/></svg>
<svg class="abs" style="left:0;top:1428px" width="1200" height="480" viewBox="0 0 1200 480"><path d="M0 0 L1200 68 L1200 340 L0 473 Z" fill="#25263a"/></svg>

<h2 class="section-title abs" style="top:663px">Every Communication Tool. <span class="light">In One place.</span></h2>

<article class="card abs" style="left:142px;top:728px">
  <svg viewBox="0 0 92 66" width="92"><path d="M22 58 H70 A18 18 0 0 0 70 22 A26 26 0 0 0 22 20 A19 19 0 0 0 22 58 Z" fill="none" stroke="#231f20" stroke-width="5"/><path d="M46 22V44M37 36L46 45L55 36" fill="none" stroke="#231f20" stroke-width="5"/></svg>
  <h3>UCaaS</h3>
  <p>Lorem ipsum dolor sit amet, consectetur adipiscing elit. Maecenas ornare lacus ut dictum pretium. Cras euismod auctor nulla, nec ullamcorper sem sodales eget. Nam</p>
  <a>Learn More &gt;</a>
</article>
<article class="card featured abs" style="left:458px;top:728px">
  <svg viewBox="0 0 92 80" width="80" style="height:80px;margin-top:-14px;margin-bottom:20px"><g fill="none" stroke="#0677BA" stroke-width="3"><rect x="12" y="44" width="66" height="28" rx="4"/><circle cx="26" cy="58" r="3"/><circle cx="37" cy="58" r="3"/><path d="M50 58H68M24 44V30M66 44V30M45 44V24"/><path d="M35 18A14 14 0 0 1 55 18M29 12A22 22 0 0 1 61 12"/></g></svg>
  <h3>SD-WAN</h3>
  <p>Lorem ipsum dolor sit amet, consectetur adipiscing elit. Maecenas ornare lacus ut dictum pretium. Cras euismod auctor nulla, nec ullamcorper sem sodales eget. Nam</p>
  <a>Learn More &gt;</a>
</article>
<article class="card abs" style="left:773px;top:728px">
  <svg viewBox="0 0 100 76" width="96" style="height:76px;margin-top:-10px;margin-bottom:20px"><g fill="none" stroke="#231f20" stroke-width="2.5"><path d="M40 8A32 28 0 1 0 22 62L8 72L34 64A32 28 0 0 0 70 40"/><path d="M18 30H50M18 40H46M18 50H40"/><path d="M52 22L96 6L72 42L64 30Z M64 30L96 6"/></g></svg>
  <h3>Business SMS/MMS</h3>
  <p>Lorem ipsum dolor sit amet, consectetur adipiscing elit. Maecenas ornare lacus ut dictum pretium. Cras euismod auctor nulla, nec ullamcorper sem sodales eget. Nam</p>
  <a>Learn More &gt;</a>
</article>

<article class="card abs" style="left:142px;top:1060px">
  <svg viewBox="0 0 96 80" width="84" style="height:80px;margin-top:-12px;margin-bottom:18px"><g fill="none" stroke="#231f20" stroke-width="2.5"><circle cx="48" cy="20" r="16"/><path d="M44 12L56 20L44 28Z"/><circle cx="22" cy="52" r="7"/><circle cx="48" cy="52" r="7"/><circle cx="74" cy="52" r="7"/><path d="M8 76A14 12 0 0 1 36 76Z M34 76A14 12 0 0 1 62 76Z M60 76A14 12 0 0 1 88 76Z"/></g></svg>
  <h3>Video Conferencing</h3>
  <p>Lorem ipsum dolor sit amet, consectetur adipiscing elit. Maecenas ornare lacus ut dictum pretium. Cras euismod auctor nulla, nec ullamcorper sem sodales eget. Nam</p>
  <a>Learn More &gt;</a>
</article>
<article class="card abs" style="left:458px;top:1060px">
  <svg viewBox="0 0 96 80" width="84" style="height:80px;margin-top:-12px;margin-bottom:18px"><g fill="none" stroke="#231f20" stroke-width="2.5"><path d="M30 30H66A10 10 0 0 0 62 12A14 14 0 0 0 36 12A10 10 0 0 0 30 30Z"/><path d="M40 30V50L22 70M46 30V70M52 30V70M58 30V50L76 70M34 30V56L16 70M64 30V56L82 70"/><circle cx="16" cy="73" r="3"/><circle cx="22" cy="73" r="3"/><circle cx="46" cy="73" r="3"/><circle cx="52" cy="73" r="3"/><circle cx="76" cy="73" r="3"/><circle cx="82" cy="73" r="3"/></g></svg>
  <h3>Managed Network Service</h3>
  <p>Lorem ipsum dolor sit amet, consectetur adipiscing elit. Maecenas ornare lacus ut dictum pretium. Cras euismod auctor nulla, nec ullamcorper sem sodales eget. Nam</p>
  <a>Learn More &gt;</a>
</article>
<article class="card abs" style="left:773px;top:1060px">
  <svg viewBox="0 0 96 80" width="90" style="height:80px;margin-top:-12px;margin-bottom:18px"><g fill="none" stroke="#231f20" stroke-width="2.5"><path d="M16 22L26 14L36 30L28 38A40 40 0 0 0 48 58L56 50L72 60L64 70C40 70 14 46 16 22Z"/><path d="M66 4A22 18 0 1 1 52 36L44 42L48 32A22 18 0 0 1 66 4Z"/><circle cx="58" cy="21" r="2.5"/><circle cx="66" cy="21" r="2.5"/><circle cx="74" cy="21" r="2.5"/></g></svg>
  <h3>Telecom</h3>
  <p>Lorem ipsum dolor sit amet, consectetur adipiscing elit. Maecenas ornare lacus ut dictum pretium. Cras euismod auctor nulla, nec ullamcorper sem sodales eget. Nam</p>
  <a>Learn More &gt;</a>
</article>

<h2 class="section-title abs" style="top:1528px;color:var(--white)">What Our Customers Say</h2>

<article class="quote-card abs" style="left:165px;top:1596px">
  <svg width="44" height="40" viewBox="0 0 44 40"><path d="M2 0H20V22L10 40H2L8 22H2Z M24 0H42V22L32 40H24L30 22H24Z" fill="var(--navy)"/></svg>
  <p>“Lorem ipsum dolor sit amet, consectetur adipiscing elit. Maecenas ornare lacus ut dictum pretium. Cras euismod auctor nulla, nec ullamcorper sem sodales eget. Nam porta tellus sit amet metus varius, congue varius dolor tincidunt. Aliquam enim leo, congue in tempor in, tincidunt vitae ante ipsum primis in faucibus. “</p>
  <h4>Office Manager</h4><small>Dubai Business</small>
</article>
<article class="quote-card featured abs" style="left:458px;top:1596px">
  <svg width="44" height="40" viewBox="0 0 44 40"><path d="M2 0H20V22L10 40H2L8 22H2Z M24 0H42V22L32 40H24L30 22H24Z" fill="var(--white)"/></svg>
  <p>“Lorem ipsum dolor sit amet, consectetur adipiscing elit. Maecenas ornare lacus ut dictum pretium. Cras euismod auctor nulla, nec ullamcorper sem sodales eget. Nam porta tellus sit amet metus varius, congue varius dolor tincidunt. Aliquam enim leo, congue in tempor in, tincidunt vitae ante ipsum primis in faucibus. “</p>
  <h4>Office Manager</h4><small>Dubai Business</small>
</article>
<article class="quote-card abs" style="left:752px;top:1596px">
  <svg width="44" height="40" viewBox="0 0 44 40"><path d="M2 0H20V22L10 40H2L8 22H2Z M24 0H42V22L32 40H24L30 22H24Z" fill="var(--navy)"/></svg>
  <p>“Lorem ipsum dolor sit amet, consectetur adipiscing elit. Maecenas ornare lacus ut dictum pretium. Cras euismod auctor nulla, nec ullamcorper sem sodales eget. Nam porta tellus sit amet metus varius, congue varius dolor tincidunt. Aliquam enim leo, congue in tempor in, tincidunt vitae ante ipsum primis in faucibus. “</p>
  <h4>Office Manager</h4><small>Dubai Business</small>
</article>

<h2 class="trial-title abs">Start Your Free Trial?</h2>
<p class="trial-text abs">Lorem ipsum dolor sit amet, consectetur adipiscing elit, sed do eiusmod tempor incididunt ut labore et dolore magna aliqua.</p>
<div class="illustration abs" role="img" aria-label="Illustration of raised hands holding smartphones with chat bubbles and video calls"></div>
<div class="field abs" style="top:2148px">Name</div>
<div class="field abs" style="top:2213px">Phone</div>
<div class="field abs" style="top:2278px">Email</div>
<div class="field select abs" style="top:2342px">Services Required<svg width="10" height="6" viewBox="0 0 10 6"><path d="M1 1L5 5L9 1" fill="none" stroke="#333" stroke-width="1.6"/></svg></div>
<div class="field abs" style="top:2399px">Address</div>
<div class="submit abs">SUBMIT NOW</div>

<footer class="site-footer abs"></footer>
<div class="footer-brand abs"><span class="brand-dot"></span>Vantrel Telecom</div>
<div class="footer-copy abs">Vantrel Telecom &nbsp;©. 2022<br>All rights reserved.</div>
<div class="divider abs" style="left:372px"></div>
<div class="footer-col abs" style="left:416px;top:2652px;color:var(--white)">
  <h5>Contact Us</h5>
  <ul><li>Toll Free: (800) 555-0142</li><li>&nbsp;Office: (415) 555-0187</li><li>&nbsp;Direct/SMS: (415) 555-0193</li><li>Email: hello@vantreltelecom.com</li></ul>
</div>
<div class="divider abs" style="left:717px"></div>
<div class="footer-col abs" style="left:756px;top:2652px;color:var(--white)">
  <h5>Useful Links</h5>
  <ul><li>Products</li><li>Integrations</li><li>Features</li><li>Pricing</li><li>Blog</li><li>Sign In</li></ul>
</div>
<div class="divider abs" style="left:925px"></div>
<div class="footer-col abs" style="left:964px;top:2652px;color:var(--white)">
  <h5>Social</h5>
  <div class="social" aria-label="Social links"><span></span><span></span><span></span></div>
</div>

</body>
</html>
```